A website for a Maltese Law Firm

Our law firm needs a website to further its business. The site should have a simple yet effective design. We would need the following sections: About us, Practice Areas, About Malta, Contact. These should be further split as follows:

About us: Our firm, Our values, What others say, Offices

Practice Areas: Crimimal, Citizenship & Residence, Harbour Passage Scheme, Criminal Defence, Civil Litigation, Arbitration and ADR, Commercial and Corporate, Media Law.

About Malta: just one section.

Contact: Just one section

We would also need a news feed at the front of the site to include latest news regarding our cases.

At the bottom we need a section for our Terms and a Privacy Statement.

Our logo is being attached.

Target Market(s)

All clients looking for legal assistance in Malta

Industry/Entity Type

Legal

Coding

Coded - Design and coding required

Number of Pages Required

1 page

Requirements
Must have
• It must be simple yet striking.

```html
<!DOCTYPE html>
<html lang="en">
<head>
<meta charset="utf-8">
<title>Darmanin &amp; Zerafa Advocates</title>
<link href="https://fonts.googleapis.com/css2?family=Roboto:wght@300;400;500;700;900&family=Roboto+Condensed:wght@400;700&display=swap" rel="stylesheet">
<style>
:root{
  --red:#c9211e;
  --red-dark:#a51a18;
  --orange:#f08a1c;
  --ink:#222;
  --muted:#777;
  --light:#f4f4f4;
  --footer:#2a2a2a;
  --footer-deep:#1b1b1b;
  --white:#fff;
}
*{box-sizing:border-box;margin:0;padding:0}
html,body{width:1200px;height:2164px;overflow:hidden}
body{font-family:"Roboto",Arial,sans-serif;color:var(--ink);background:var(--white);font-size:12px;line-height:1.5}
section,header,footer{position:relative;width:1200px}
.topbar{height:24px;background:var(--red-dark);color:var(--white);font-size:10px;display:flex;align-items:center;padding:0 100px;gap:34px}
.topbar span{display:flex;align-items:center;gap:5px}
.topbar .social{margin-left:auto;display:flex;gap:6px}
.topbar .social i{width:12px;height:12px;background:rgba(255,255,255,.35);display:block}
.nav{height:56px;background:var(--white);display:flex;align-items:center;justify-content:center;border-bottom:1px solid #e4e4e4}
.nav a{font-family:"Roboto Condensed",Arial,sans-serif;font-size:12px;font-weight:700;color:var(--ink);text-decoration:none;padding:0 16px;height:56px;display:flex;align-items:center;text-transform:uppercase}
.nav a.active{background:var(--red);color:var(--white)}
.brand{margin:0 40px;text-align:center;font-family:"Roboto",Arial,sans-serif;font-weight:500;color:var(--ink);font-size:20px;line-height:1.1;letter-spacing:1px;display:flex;align-items:center;gap:10px}
.brand i{width:10px;height:10px;background:var(--red);display:block}
.hero{height:464px;background:linear-gradient(90deg,#4a4a4a 0%,#8a8a8a 45%,#d0d0d0 70%,#9a9a9a 100%)}
.hero-copy{position:absolute;left:100px;top:168px;color:var(--white)}
.hero h1{font-size:34px;font-weight:900;line-height:1.15;text-transform:uppercase;display:inline-block;background:rgba(0,0,0,.35);padding:4px 8px}
.hero p{font-size:13px;margin:10px 0 16px;max-width:300px}
.btn{display:inline-block;background:var(--orange);color:var(--white);font-weight:700;font-size:11px;padding:9px 18px;text-transform:uppercase}
.hero .btn{background:var(--red)}
.welcome{height:216px;text-align:center;padding-top:50px}
.welcome h2{font-size:22px;font-weight:700;text-transform:uppercase}
.welcome h2:after{content:"";display:block;width:50px;height:3px;background:var(--red);margin:10px auto 14px}
.welcome p{font-size:11px;color:var(--muted);max-width:720px;margin:0 auto}
.practice{height:320px;padding:16px 100px 0}
.section-head{display:flex;align-items:center;gap:16px;margin-bottom:22px}
.section-head h2{font-size:20px;font-weight:700;text-transform:uppercase;white-space:nowrap}
.section-head p{font-size:10px;color:var(--muted)}
.cards{display:flex;gap:14px}
.card{width:240px;height:218px;position:relative;background:linear-gradient(135deg,#6d6d6d,#c9c9c9)}
.card:nth-child(2){background:linear-gradient(135deg,#8b7a66,#d8d0c4)}
.card:nth-child(3){background:linear-gradient(135deg,#5a6a80,#cfd8e2)}
.card:nth-child(4){background:linear-gradient(135deg,#7f93a6,#e6ecf1)}
.card .label{position:absolute;left:0;bottom:20px;background:var(--red);color:var(--white);padding:6px 12px 5px;font-weight:700;font-size:12px;text-transform:uppercase;line-height:1.2}
.card .label small{display:block;font-weight:400;font-size:9px;text-transform:none}
.about{height:340px;padding:20px 100px 0;display:flex;gap:40px}
.portrait{width:380px;height:280px;background:linear-gradient(160deg,#3c3c3c,#9d9d9d)}
.about-copy{padding-top:6px;width:680px}
.about-copy h2{font-size:20px;font-weight:700;text-transform:uppercase}
.about-copy h2:after{content:"";display:block;width:50px;height:3px;background:var(--red);margin:8px 0 12px}
.about-copy p{font-size:11px;color:var(--muted);margin-bottom:10px}
.band{height:320px;background:var(--red);color:var(--white);padding:40px 100px 0;display:flex;gap:40px}
.band h3{font-size:18px;font-weight:700;text-transform:uppercase;margin-bottom:14px}
.malta{width:340px}
.video{width:300px;height:170px;background:linear-gradient(135deg,#5b3a2a,#c59b72);position:relative}
.video svg{position:absolute;left:130px;top:65px}
.malta p{font-size:11px;margin-top:10px;width:300px}
.news{flex:1}
.news-grid{display:grid;grid-template-columns:1fr 1fr;gap:14px 30px}
.news-item{display:flex;gap:12px;align-items:flex-start}
.news-item .thumb{width:88px;height:58px;background:linear-gradient(135deg,#444,#bbb);flex:none}
.news-item p{font-size:10px;font-weight:700;text-transform:uppercase;line-height:1.35}
.news-item small{display:block;font-weight:400;text-transform:none;font-size:9px;opacity:.85;margin-top:3px}
.footer{height:308px;background:var(--footer);color:#bbb;padding:36px 100px 0}
.cols{display:flex;gap:60px}
.col h4{color:var(--white);font-size:12px;font-weight:700;text-transform:uppercase;margin-bottom:12px}
.col li{list-style:none;font-size:10px;line-height:2}
.contact li{display:flex;align-items:center;gap:6px}
.footer .brand{color:var(--white);margin:18px 0 0;font-size:16px;justify-content:flex-start}
.copyright{position:absolute;right:100px;bottom:14px;font-size:9px;color:#999}
.bottom{height:116px;background:var(--footer-deep);color:#888;font-size:9px;padding:20px 100px}
.bottom b{color:#ccc}
</style>
</head>
<body>
<header>
  <div class="topbar">
    <span><svg width="10" height="10" viewBox="0 0 10 10"><path d="M2 1l2 2-1 1.5c.7 1.3 1.3 1.9 2.5 2.5L7 6l2 2-1.5 1.5C4.5 9 1 5.5.5 2.5z" fill="#fff"/></svg>(+356) 2100 4410</span>
    <span><svg width="10" height="10" viewBox="0 0 10 10"><path d="M2 1l2 2-1 1.5c.7 1.3 1.3 1.9 2.5 2.5L7 6l2 2-1.5 1.5C4.5 9 1 5.5.5 2.5z" fill="#fff"/></svg>(+356) 2100 4411 Valletta</span>
    <span><svg width="10" height="10" viewBox="0 0 10 10"><path d="M2 1l2 2-1 1.5c.7 1.3 1.3 1.9 2.5 2.5L7 6l2 2-1.5 1.5C4.5 9 1 5.5.5 2.5z" fill="#fff"/></svg>(+356) 2100 4412 Gozo</span>
    <span><svg width="11" height="9" viewBox="0 0 11 9"><rect x=".5" y=".5" width="10" height="8" fill="none" stroke="#fff"/><path d="M.5.5l5 4 5-4" fill="none" stroke="#fff"/></svg>info@dzadvocates.mt</span>
    <div class="social"><i></i><i></i><i></i></div>
  </div>
  <nav class="nav">
    <a href="#">Home</a><a href="#">About Us</a><a href="#" class="active">Practice Areas</a>
    <div class="brand"><i></i>DARMANIN &amp; ZERAFA</div>
    <a href="#">About Malta</a><a href="#">Contact Us</a>
  </nav>
</header>

<section class="hero" role="img" aria-label="Lawyer signing documents at a desk">
  <div class="hero-copy">
    <h1>We are a law firm<br>from Malta</h1>
    <p>Lorem ipsum is simply dummy text of the printing and typesetting industry</p>
    <span class="btn">Contact Today</span>
  </div>
</section>

<section class="welcome">
  <h2>Welcome to DZ Advocates</h2>
  <p>Lorem ipsum is simply dummy text of the printing and typesetting industry. Lorem ipsum has been the industry's standard dummy text ever since the 1500s, when an unknown printer took a galley of type and scrambled it to make a type specimen book.</p>
</section>

<section class="practice">
  <div class="section-head">
    <h2>Practice Areas</h2>
    <p>Lorem ipsum is simply dummy text of the printing and typesetting industry. Lorem ipsum has been the industry's standard.</p>
  </div>
  <div class="cards">
    <div class="card" role="img" aria-label="Handcuffed hands"><div class="label">Criminal<small>Click here for more info</small></div></div>
    <div class="card" role="img" aria-label="Passport and residence documents"><div class="label">Citizenship &amp; Residence<small>Click here for more info</small></div></div>
    <div class="card" role="img" aria-label="Business people shaking hands"><div class="label">Harbour Passage Scheme<small>Click here for more info</small></div></div>
    <div class="card" role="img" aria-label="Office towers against the sky"></div>
  </div>
</section>

<section class="about">
  <div class="portrait" role="img" aria-label="Portrait of a lawyer in a suit"></div>
  <div class="about-copy">
    <h2>About DZ Advocates</h2>
    <p>Lorem ipsum is simply dummy text of the printing and typesetting industry. Lorem ipsum has been the industry's standard dummy text ever since the 1500s, when an unknown printer took a galley of type and scrambled it to make a type specimen book.</p>
    <p>It has survived not only five centuries, but also the leap into electronic typesetting, remaining essentially unchanged. It was popularised in the 1960s with the release of Letraset sheets containing passages.</p>
    <span class="btn">Read More</span>
  </div>
</section>

<section class="band">
  <div class="malta">
    <h3>About Malta</h3>
    <div class="video" role="img" aria-label="Video still of Maltese harbour">
      <svg width="40" height="40" viewBox="0 0 40 40"><rect width="40" height="40" rx="4" fill="#c9211e"/><path d="M15 11l14 9-14 9z" fill="#fff"/></svg>
    </div>
    <p>Lorem ipsum is simply dummy text of the printing and typesetting industry by the industry.</p>
  </div>
  <div class="news">
    <h3>Latest News</h3>
    <div class="news-grid">
      <div class="news-item"><div class="thumb" role="img" aria-label="News photo"></div><p>Lorem ipsum is simply dummy text of the printing<small>Posted on 17 March 2016</small></p></div>
      <div class="news-item"><div class="thumb" role="img" aria-label="News photo"></div><p>Lorem ipsum is simply dummy text of the printing<small>Posted on 17 March 2016</small></p></div>
      <div class="news-item"><div class="thumb" role="img" aria-label="News photo"></div><p>Lorem ipsum is simply dummy text of the printing<small>Posted on 17 March 2016</small></p></div>
      <div class="news-item"><div class="thumb" role="img" aria-label="News photo"></div><p>Lorem ipsum is simply dummy text of the printing<small>Posted on 17 March 2016</small></p></div>
      <div class="news-item"><div class="thumb" role="img" aria-label="News photo"></div><p>Lorem ipsum is simply dummy text of the printing<small>Posted on 17 March 2016</small></p></div>
      <div class="news-item"><div class="thumb" role="img" aria-label="News photo"></div><p>Lorem ipsum is simply dummy text of the printing<small>Posted on 17 March 2016</small></p></div>
    </div>
  </div>
</section>

<footer class="footer">
  <div class="cols">
    <div class="col"><h4>Welcome</h4><ul><li>Home</li><li>About Us</li><li>Practice Areas</li><li>About Malta</li><li>Contact Us</li></ul></div>
    <div class="col"><h4>Practice Areas</h4><ul><li>Criminal</li><li>Citizenship &amp; Residence</li><li>Harbour Passage Scheme</li><li>Criminal Defence</li><li>Civil Litigation</li><li>Arbitration and ADR</li><li>Commercial and Corporate</li><li>Media Law</li></ul></div>
    <div class="col"><h4>Information</h4><ul><li>Terms &amp; Conditions</li><li>Privacy Statement</li><li>Disclaimer</li><li>Sitemap</li></ul></div>
    <div class="col contact"><h4>Contact Info</h4><ul><li>14 Merchants Street</li><li>Valletta VLT 1170</li><li>Malta</li></ul><div class="brand"><i></i>DARMANIN &amp; ZERAFA</div></div>
    <div class="col contact"><h4>&nbsp;</h4><ul><li>(+356) 2100 4410</li><li>(+356) 2100 4411 Valletta</li><li>(+356) 2100 4412 Gozo</li><li>(+356) 2100 4413</li><li>info@dzadvocates.mt</li></ul></div>
  </div>
  <div class="copyright">Copyright © 2016, DZ Advocates. All rights reserved.</div>
</footer>

<div class="bottom">
  <p><b>Terms and privacy statement</b> – Lorem ipsum is simply dummy text of the printing and typesetting industry. Lorem ipsum has been the industry's standard dummy text ever since the 1500s, when an unknown printer took a galley of type and scrambled it to make a type specimen book. It has survived not only five centuries.</p>
</div>
</body>
</html>
```